Business Card Design - CPA Firm

Need a Business Card for my CPA Firm. I'd like to include both my favicon (perhaps front) and Logo (perhaps back) on the card.

I'll attach my Brand Template (includes font and color), Logo and Favicon.

I'd like a beach and palm tree image/resemblance in the design.
Updates

Please see additional notes I've added.

Rosalind M. Vantrecourt, CPA
CPA@LedgerhouseofSeagroveShores.example
Servicing Palm Beach & Beyond
West Palm Beach, FL 33417
(555) 748-2916

Target Market(s)

Small Business Owners, Entrepreneurs and Professions.

Industry/Entity Type

Accounting/ CPA Firm

Contact Information for Business Card

We empower businesses and professionals for success through our strategic accounting solutions!

Requirements
Must have
• Branding: Font, Colors, Logo and Favicon
Nice to have
• For address: Servicing Seagrove Coast & Beyond, Seagrove Shores, FL 30000
Should not have
• My Physical Street Address (see "Nice to Haves")

```html
<!DOCTYPE html>
<html lang="en">
<head>
<meta charset="utf-8">
<title>Ledgerhouse of Seagrove Shores – Business Card</title>
<link href="https://fonts.googleapis.com/css2?family=Cinzel:wght@600;700&family=Raleway:wght@500;600;700&display=swap" rel="stylesheet">
<style>
  :root {
    --navy: #1f2c7a;
    --navy-deep: #18205c;
    --teal: #1aa59a;
    --teal-deep: #178b86;
    --gold: #e4a82a;
    --sun: #f6c516;
    --ink: #3a3a3a;
    --paper: #ffffff;
    --mist: #f2f2f2;
    --stage: #e9e5df;
    --sea: #a9d6c6;
    --sand: #f7f7f3;
    --palm: #4f8a3a;
  }
  * { box-sizing: border-box; margin: 0; padding: 0; }
  html, body { width: 1200px; height: 977px; overflow: hidden; }
  body { background: var(--stage); position: relative; font-family: "Raleway", sans-serif; }

  .card {
    position: absolute;
    width: 600px;
    height: 343px;
    border-radius: 22px;
    overflow: hidden;
    background: var(--paper);
    box-shadow: 0 10px 28px rgba(0,0,0,.18);
  }
  .card--front { left: 90px; top: 100px; }
  .card--back  { left: 510px; top: 530px; }

  /* Front */
  .beach-photo {
    position: absolute; inset: 0;
    background:
      linear-gradient(200deg, transparent 55%, rgba(79,138,58,.75) 75%, rgba(79,138,58,.55) 100%),
      linear-gradient(180deg, var(--sea) 0%, #cfe7dd 30%, var(--sand) 55%, #eeeeea 100%);
  }
  .front-lockup {
    position: absolute; left: 0; right: 0; top: 112px;
    text-align: center;
  }

  /* Brand name lockup */
  .brand {
    display: inline-flex; align-items: center; gap: 12px;
  }
  .brand__dot {
    width: 30px; height: 30px; border-radius: 50%;
    background: var(--sun); flex: none;
  }
  .brand__name {
    font-family: "Cinzel", serif; font-weight: 700;
    color: var(--navy); line-height: 1.05; text-align: left;
  }
  .card--front .brand__name { font-size: 30px; }
  .brand__tagline {
    font-family: "Raleway", sans-serif; font-weight: 600;
    color: var(--navy); letter-spacing: .18em; text-transform: uppercase;
    font-size: 10px; margin-top: 10px;
  }

  /* Back */
  .backdrop-circle {
    position: absolute; right: -60px; top: 40px;
    width: 330px; height: 330px; border-radius: 50%;
    background: var(--mist);
  }
  .back-lockup { position: absolute; left: 52px; top: 70px; }
  .card--back .brand__name { font-size: 21px; }
  .card--back .brand__dot { width: 24px; height: 24px; }
  .card--back .brand__tagline { font-size: 8.5px; margin-left: 36px; margin-top: 8px; }

  .person { position: absolute; left: 52px; top: 176px; }
  .person__name {
    font-family: "Cinzel", serif; font-weight: 700;
    font-size: 25px; color: var(--navy); line-height: 1;
  }
  .person__role { font-size: 15px; font-weight: 500; color: var(--gold); margin-top: 6px; }

  .contact {
    position: absolute; left: 360px; top: 82px;
    list-style: none; font-size: 12.5px; font-weight: 500; color: var(--ink);
  }
  .contact li { display: flex; align-items: center; gap: 9px; height: 24px; }
  .contact svg { width: 13px; height: 13px; fill: var(--gold); flex: none; }

  .stripe {
    position: absolute; left: 0; right: 0; top: 256px; height: 9px;
    display: flex;
  }
  .stripe span { flex: 1; }
  .stripe span:nth-child(1) { background: var(--navy-deep); }
  .stripe span:nth-child(2) { background: var(--navy); }
  .stripe span:nth-child(3) { background: var(--teal-deep); }
  .stripe span:nth-child(4) { background: var(--teal); }
  .stripe span:nth-child(5) { background: var(--gold); }
  .stripe span:nth-child(6) { background: var(--sun); }

  .service-area {
    position: absolute; left: 0; right: 0; top: 284px;
    text-align: center; font-weight: 700; font-size: 14px;
    letter-spacing: .02em; text-transform: uppercase; color: var(--navy);
  }
</style>
</head>
<body>

<section class="card card--front">
  <div class="beach-photo" role="img" aria-label="Aerial view of turquoise sea, white sand beach with umbrellas and a row of palm trees"></div>
  <div class="front-lockup">
    <div class="brand">
      <span class="brand__dot"></span>
      <span class="brand__name">Ledgerhouse<br>of Seagrove Shores</span>
    </div>
    <p class="brand__tagline">Licensed CPA Firm</p>
  </div>
</section>

<section class="card card--back">
  <div class="backdrop-circle"></div>

  <div class="back-lockup">
    <div class="brand">
      <span class="brand__dot"></span>
      <span class="brand__name">Ledgerhouse<br>of Seagrove Shores</span>
    </div>
    <p class="brand__tagline">Licensed CPA Firm</p>
  </div>

  <div class="person">
    <p class="person__name">Marcus Delano</p>
    <p class="person__role">Founder &amp; CEO</p>
  </div>

  <ul class="contact">
    <li>
      <svg viewBox="0 0 24 24" aria-hidden="true"><path d="M6.6 10.8a15 15 0 0 0 6.6 6.6l2.2-2.2a1 1 0 0 1 1-.25 11.4 11.4 0 0 0 3.6.57 1 1 0 0 1 1 1V20a1 1 0 0 1-1 1A17 17 0 0 1 3 4a1 1 0 0 1 1-1h3.5a1 1 0 0 1 1 1c0 1.25.2 2.45.57 3.57a1 1 0 0 1-.25 1z"/></svg>
      (555) 310-4482
    </li>
    <li>
      <svg viewBox="0 0 24 24" aria-hidden="true"><path d="M7 1h10a2 2 0 0 1 2 2v18a2 2 0 0 1-2 2H7a2 2 0 0 1-2-2V3a2 2 0 0 1 2-2zm0 3v14h10V4zm5 15.5a1.2 1.2 0 1 0 0 2.4 1.2 1.2 0 0 0 0-2.4z"/></svg>
      (555) 627-1905
    </li>
    <li>
      <svg viewBox="0 0 24 24" aria-hidden="true"><path d="M2 5h20v14H2zm2 2v.5l8 5 8-5V7zm0 2.8V17h16V9.8l-8 5z"/></svg>
      info@seagroveledger.example
    </li>
    <li>
      <svg viewBox="0 0 24 24" aria-hidden="true"><path d="M12 2a10 10 0 1 0 0 20 10 10 0 0 0 0-20zm6.9 6h-3a15.7 15.7 0 0 0-1.4-3.6A8 8 0 0 1 18.9 8zM12 4c.8 1.200 1.5 2.5 1.9 4h-3.8c.4-1.5 1.1-2.8 1.900-4zM4.3 14a8 8 0 0 1 0-4h3.4a16.5 16.5 0 0 0 0 4zm.8 2h3a15.7 15.7 0 0 0 1.4 3.6A8 8 0 0 1 5.1 16zm3-8h-3a8 8 0 0 1 4.4-3.6A15.7 15.7 0 0 0 8.1 8zM12 20c-.8-1.2-1.5-2.5-1.9-4h3.8c-.4 1.5-1.1 2.8-1.9 4zm2.3-6H9.7a14.7 14.7 0 0 1 0-4h4.6a14.7 14.7 0 0 1 0 4zm.2 5.6a15.7 15.7 0 0 0 1.4-3.6h3a8 8 0 0 1-4.4 3.6zm1.8-5.6a16.5 16.5 0 0 0 0-4h3.4a8 8 0 0 1 0 4z"/></svg>
      seagroveledger.example
    </li>
  </ul>

  <div class="stripe" aria-hidden="true">
    <span></span><span></span><span></span><span></span><span></span><span></span>
  </div>

  <p class="service-area">Servicing Seagrove Coast &amp; Beyond, Seagrove Shores, FL 30000</p>
</section>

</body>
</html>
```